Music Festival in Colorado Needs Awesome Flier Design

We need an eye-catching & captivating flier design for an annual music festival in Denver, CO (USA). The festival features the best Colorado musicians within the genres of jam - funk - bluegrass - electronic - reggae - rock.

The design should look clean and professional while still being creative and unique. The past three years' flier designs are attached, as well as the logo and some other designs that match the aesthetic of what we're looking for.

This festival has a big element of Colorado pride so any

Target Market(s)

Hippies - live music enthusiasts - partiers. Ages 21 - 40.

Industry/Entity Type

Entertainment

Colors
0355a3
ec1f27
ffffff
fbed22

Requirements
Must have
• Attached design text.
Nice to have
• - Quality texture and psychedelic elements.
• - Colorado pride elements; color scheme (red, white, blue & yellow), flag, ect.
• - Nature elements are awesome but this is also a downtown festival so keep that in mind.
Should not have
• Cheesy artwork.

```html
<!DOCTYPE html>
<html lang="en">
<head>
<meta charset="utf-8">
<title>Pass The Word Music Festival 2018</title>
<link rel="stylesheet" href="https://fonts.googleapis.com/css2?family=Chewy&family=Roboto+Condensed:wght@700&display=swap">
<style>
  :root {
    --white: #ffffff;
    --ink: #0b1020;
    --deep-blue: #0b1a4a;
    --violet: #3a1a6e;
    --sky: #4a6fb0;
    --stone: #7c7a6e;
    --sun: #fbed22;
    --flame: #ec1f27;
    --teal-night: #0e2a2e;
  }
  * { margin: 0; padding: 0; box-sizing: border-box; }
  html, body { width: 776px; height: 1200px; overflow: hidden; background: var(--ink); }
  .flier {
    position: relative;
    width: 776px;
    height: 1200px;
    overflow: hidden;
    font-family: "Roboto Condensed", "Arial Narrow", sans-serif;
    font-weight: 700;
    color: var(--white);
  }
  .backdrop {
    position: absolute;
    inset: 0;
    background:
      radial-gradient(ellipse 240px 330px at 50% 62%, rgba(251,237,34,.85), rgba(246,140,30,.55) 45%, rgba(236,31,39,0) 80%),
      radial-gradient(ellipse 380px 460px at 50% 66%, rgba(236,31,39,.55), rgba(120,40,140,.35) 55%, rgba(0,0,0,0) 85%),
      linear-gradient(180deg,
        var(--violet) 0%,
        var(--deep-blue) 9%,
        #2c3f86 16%,
        var(--sky) 22%,
        var(--stone) 32%,
        #6a6a5e 42%,
        #4a5660 55%,
        #2e3e48 72%,
        var(--teal-night) 88%,
        #081418 100%);
  }
  .title {
    position: absolute;
    left: 0; right: 0;
    text-align: center;
    font-family: "Chewy", "Comic Sans MS", cursive;
    font-weight: 400;
    font-size: 42px;
    line-height: 1;
    letter-spacing: 1px;
    color: var(--white);
    -webkit-text-stroke: 2px var(--ink);
    paint-order: stroke fill;
    text-shadow: 0 3px 6px rgba(0,0,0,.6);
  }
  .title--name { top: 44px; }
  .title--dates { top: 97px; }
  .brand {
    position: absolute;
    top: 222px;
    left: 0; right: 0;
    display: flex;
    justify-content: center;
    align-items: center;
    gap: 18px;
  }
  .brand__mark {
    width: 34px; height: 34px;
    background: var(--white);
  }
  .brand__name {
    font-size: 76px;
    line-height: 1;
    letter-spacing: 1px;
    color: var(--white);
  }
  .lineup {
    position: absolute;
    top: 441px;
    left: 0; right: 0;
    list-style: none;
    text-align: center;
  }
  .lineup__row {
    font-size: 25px;
    line-height: 39px;
    white-space: nowrap;
    text-shadow: 0 2px 3px rgba(0,0,0,.85), 0 0 6px rgba(0,0,0,.5);
  }
  .info {
    position: absolute;
    font-style: normal;
    text-shadow: 0 2px 3px rgba(0,0,0,.8);
  }
  .info--tickets { left: 32px; top: 1118px; font-size: 19px; line-height: 31px; }
  .info--venue { right: 32px; top: 1106px; text-align: right; font-size: 16px; line-height: 24px; }
</style>
</head>
<body>
<main class="flier">
  <div class="backdrop" role="img" aria-label="Psychedelic fractal sky over Colorado mountains and a canyon, with a rainbow glow rising from the centre"></div>

  <h1 class="title title--name">Pass The Word Music Festival</h1>
  <p class="title title--dates">May 11th - 13th, 2018 (6th Annual)</p>

  <div class="brand">
    <span class="brand__mark"></span>
    <span class="brand__name">PASS THE WORD</span>
  </div>

  <ul class="lineup">
    <li class="lineup__row">Jess Alder Band - Every Hour Orchestra - Break Signal</li>
    <li class="lineup__row">The Copper Beans - J-Rod &amp; The Ridge</li>
    <li class="lineup__row">DeadFish Orchestra - Tamarack, Dynoseeker</li>
    <li class="lineup__row">WildWater Ramble - Evidence Ensemble - Analog Sun</li>
    <li class="lineup__row">The Grain Farm - Skywoven - Everhoff - Gemstones - Polyculture</li>
    <li class="lineup__row">Rail Station - Metasonics - Spectrum - Lucid Lantern</li>
    <li class="lineup__row">Rail Station - Circuits - The Sweet Sorrels - Jyvo Club</li>
    <li class="lineup__row">Jade Carver Band - Atomica - Rootsasaurus</li>
    <li class="lineup__row">Tortlefield, Other Blue - The Workday - Mama Marigold</li>
    <li class="lineup__row">Ninth Peak Division - Amarilla - Envy Ode</li>
    <li class="lineup__row">Boogie Mastodon - Casual Captain - Micah Thunder</li>
    <li class="lineup__row">Wabanaki Set - Project 528 - Apex Wave - Kalidoscope</li>
    <li class="lineup__row">Cody Russo &amp; The Soul Shed</li>
    <li class="lineup__row">Lulu Rising - Ninth Peak Division - Mlango</li>
  </ul>

  <p class="info info--tickets">Tickets &amp; More Info:<br>www.passthewordfest.com</p>
  <address class="info info--venue">Fern Street Yard<br>418 W. 52nd Ave<br>Denver, CO 80221</address>
</main>
</body>
</html>
```